Outdoor Company Business Card design

We are an outdoor adventure company needing a business card. We sell outdoor adventures and clothing. Please use our logo in the business card. We are looking for something unique but delivers a clear message as to who we are. Please be creative

Target Market(s)

Outdoor adventures

Industry/Entity Type

Business

Contact Information for Business Card

Business name: TrailBirch If using the logo, no need to have a spot for the name
Owner / CEO: Ross Dalby
Website: TrailBirch.example
Facebook: Campfeed.example/TrailBirch
Instagram: @dalby_ross
phone number: 555-304-7192
Email: Dalbycrew@TrailBirch.example

Colors

Designer to choose colors to be used in the design.

Requirements
Must have
• The business card must include the details mentioned above. ie logo, my name, email, facebook, instagram, website, and phone number.
Should not have
• should not be cluttered or look messy

```html
<!DOCTYPE html>
<html lang="en">
<head>
<meta charset="utf-8">
<title>TrailBirch Business Card</title>
<link href="https://fonts.googleapis.com/css2?family=Montserrat:wght@400;500;600;700&display=swap" rel="stylesheet">
<style>
  :root {
    --backdrop: #e9e9e7;
    --card-dark: #2b2b2c;
    --card-light: #fafafa;
    --ink: #2a2a2a;
    --brand-blue: #2a73c2;
    --brand-orange: #e8582a;
    --muted: #3a3a3a;
  }
  * { box-sizing: border-box; margin: 0; padding: 0; }
  html, body {
    width: 1200px; height: 869px; overflow: hidden;
    background: var(--backdrop);
    font-family: "Montserrat", sans-serif;
  }
  .sheet {
    width: 1200px; height: 869px;
    display: flex; align-items: center; justify-content: center; gap: 44px;
  }
  .card {
    width: 530px; height: 303px;
    border-radius: 26px;
    position: relative;
    box-shadow: 0 10px 28px rgba(0,0,0,0.18);
    overflow: hidden;
  }
  .card--front {
    background: var(--card-dark);
    display: flex; flex-direction: column; align-items: center; justify-content: center;
    gap: 26px;
  }
  .brand { display: flex; align-items: center; gap: 14px; }
  .brand__dot {
    width: 30px; height: 30px; border-radius: 50%;
    background: var(--brand-blue); flex: none;
  }
  .brand__name {
    font-weight: 600; font-size: 44px; letter-spacing: 1px;
    color: var(--brand-blue); text-transform: uppercase; white-space: nowrap;
  }
  .front__site {
    font-size: 15px; font-weight: 500; letter-spacing: 1.5px;
    color: var(--brand-orange); text-transform: uppercase;
  }
  .card--back { background: var(--card-light); padding: 34px 38px; }
  .person__name {
    font-size: 25px; font-weight: 500; letter-spacing: 2px;
    color: var(--ink); text-transform: uppercase;
  }
  .person__title {
    margin-top: 4px;
    font-size: 13px; font-weight: 500; letter-spacing: 1.5px;
    color: var(--brand-orange); text-transform: uppercase;
  }
  .contacts { margin-top: 24px; list-style: none; display: grid; gap: 8px; }
  .contact {
    display: flex; align-items: center; gap: 11px;
    font-size: 14px; font-weight: 500; color: var(--muted); white-space: nowrap;
  }
  .contact__icon { width: 14px; height: 14px; flex: none; }
  .back__brand {
    position: absolute; right: 36px; bottom: 30px;
    display: flex; align-items: center; gap: 10px;
  }
  .back__brand .brand__dot { width: 20px; height: 20px; }
  .back__brand .brand__name { font-size: 30px; }
</style>
</head>
<body>
<main class="sheet">
  <section class="card card--front" aria-label="Card front">
    <div class="brand">
      <span class="brand__dot"></span>
      <span class="brand__name">TrailBirch</span>
    </div>
    <p class="front__site">TrailBirch.example</p>
  </section>

  <section class="card card--back" aria-label="Card back">
    <h1 class="person__name">Ross Dalby</h1>
    <p class="person__title">Owner / CEO</p>
    <ul class="contacts">
      <li class="contact">
        <svg class="contact__icon" viewBox="0 0 14 14"><path d="M3 1h2.2l1 3-1.4 1a7 7 0 0 0 3.2 3.2l1-1.4 3 1V11a2 2 0 0 1-2 2A11 11 0 0 1 1 3a2 2 0 0 1 2-2z" fill="var(--brand-blue)"/></svg>
        555-304-7192
      </li>
      <li class="contact">
        <svg class="contact__icon" viewBox="0 0 14 14"><rect x="0.5" y="2.5" width="13" height="9" rx="1" fill="var(--brand-blue)"/><path d="M1 3.5l6 4.2 6-4.2" stroke="#fff" stroke-width="1.2" fill="none"/></svg>
        Dalbycrew@TrailBirch.example
      </li>
      <li class="contact">
        <svg class="contact__icon" viewBox="0 0 14 14"><rect x="1" y="1" width="12" height="12" rx="2" fill="var(--brand-blue)"/></svg>
        Campfeed.example/TrailBirch
      </li>
      <li class="contact">
        <svg class="contact__icon" viewBox="0 0 14 14"><rect x="1" y="1" width="12" height="12" rx="2" fill="var(--brand-blue)"/></svg>
        @dalby_ross
      </li>
    </ul>
    <div class="back__brand">
      <span class="brand__dot"></span>
      <span class="brand__name">TrailBirch</span>
    </div>
  </section>
</main>
</body>
</html>
```